Consulting company needs Business Cards - rough concept provided

I'm looking for someone to take our business card idea and make is slick and polished - to communicate our high-end, sophisticated, serious consulting business. We have a rough layout we did in-house. We are open to ideas on repo-ing elements, adjusting sizes, typefaces etc... within the general concept we've already come up with. We want it to be super-clean and sophisticated. We want to keep the white backgrounds, and blue brand colors. Our goal is to print with painted blue edges on thick cardstock. Thank you!!

```html
<!DOCTYPE html>
<html lang="en">
<head>
<meta charset="utf-8">
<title>Brightmere Business Cards</title>
<link href="https://fonts.googleapis.com/css2?family=Lato:wght@400;700;900&family=Raleway:wght@200;800&display=swap" rel="stylesheet">
<style>
  :root {
    --brand-blue: #009cdc;
    --ink: #111111;
    --paper: #ffffff;
    --backdrop: #2b2b2b;
  }
  * { margin: 0; padding: 0; box-sizing: border-box; }
  html, body { width: 1200px; height: 875px; overflow: hidden; background: var(--backdrop); }
  .canvas { position: relative; width: 1200px; height: 875px; }

  .card {
    position: absolute;
    width: 530px;
    height: 303px;
    border-radius: 24px;
    overflow: hidden;
  }

  /* Back of card: statement */
  .card-back {
    left: 45px; top: 286px;
    background: var(--brand-blue);
    color: var(--paper);
    padding: 54px 44px;
  }
  .statement {
    font-family: "Raleway", sans-serif;
    font-weight: 200;
    font-size: 30px;
    line-height: 1.38;
  }
  .statement strong { font-weight: 800; }

  /* Front of card */
  .card-front {
    left: 625px; top: 286px;
    background: var(--brand-blue);
  }
  .card-front .wave { position: absolute; inset: 0; width: 100%; height: 100%; }
  .wordmark {
    position: absolute;
    right: 22px; top: 14px;
    font-family: "Lato", sans-serif;
    font-weight: 900;
    font-size: 44px;
    letter-spacing: -1px;
    color: var(--brand-blue);
    line-height: 1;
  }
  .person {
    position: absolute;
    left: 30px; bottom: 28px;
    font-family: "Lato", sans-serif;
    color: var(--paper);
  }
  .person-name { font-weight: 700; font-size: 22px; }
  .person-role { font-weight: 400; font-size: 13px; margin-top: 2px; }
  .contact {
    position: absolute;
    right: 24px; top: 142px;
    font-family: "Lato", sans-serif;
    font-size: 11.5px;
    line-height: 1.6;
    color: var(--paper);
    text-align: right;
  }
  .contact-line { display: flex; align-items: center; justify-content: flex-end; gap: 8px; }
  .contact-icon { width: 13px; height: 13px; }
  .contact-address { margin-top: 8px; padding-right: 21px; }
</style>
</head>
<body>
<main class="canvas">

  <section class="card card-back">
    <p class="statement"><strong>We help</strong> [target demogrphic] <strong>achieve</strong> [desired emotional outcome] <strong>By</strong> Unique approach]<strong>because</strong>[Our Brand beliefs]</p>
  </section>

  <section class="card card-front">
    <svg class="wave" viewBox="0 0 530 303" preserveAspectRatio="none" aria-hidden="true">
      <path class="wave-field" d="M0 0 H530 V76 C440 70 370 80 320 140 C260 205 160 222 40 182 L0 170 Z" fill="var(--paper)"/>
      <path class="wave-edge" d="M530 84 C445 80 385 92 332 152 C270 222 160 236 40 182" fill="none" stroke="var(--paper)" stroke-width="5"/>
      <path class="wave-stripe" d="M40 182 C160 222 260 205 320 140 C370 80 440 70 530 76 L530 84 C445 80 385 92 332 152 C270 222 160 236 40 182 Z" fill="var(--ink)"/>
    </svg>
    <div class="wordmark">BRIGHTMERE</div>
    <div class="contact">
      <div class="contact-line">(555) 210 4837
        <svg class="contact-icon" viewBox="0 0 16 16" aria-hidden="true"><path d="M3 1 L6 1 L7 5 L5 6.5 C6 9 7 10 9.5 11 L11 9 L15 10 V13 C15 14 14 15 13 15 C6 15 1 10 1 3 C1 2 2 1 3 1 Z" fill="var(--paper)"/></svg>
      </div>
      <div class="contact-line">dana@brightmere.com
        <svg class="contact-icon" viewBox="0 0 16 16" aria-hidden="true"><rect x="1" y="3" width="14" height="10" fill="var(--paper)"/><path d="M1 3 L8 9 L15 3" fill="none" stroke="var(--brand-blue)" stroke-width="1.3"/></svg>
      </div>
      <div class="contact-address">4820 Alder Park Way, Ste 210<br>Marlow Hill, CA 90210</div>
    </div>
    <div class="person">
      <div class="person-name">Dana Whitlow</div>
      <div class="person-role">Brand Consultant</div>
    </div>
  </section>

</main>
</body>
</html>
```